Indianapolis based store looking for a multi-page website, to include ecommerce. We sell Heron mattresses, which are manufactured in Fort Wayne, Indiana. The design line of mattresses includes the blue heron (value), white heron (mid-value) and night heron (high end). We also offer mattresses for RV, futon and pet mattresses. We want a user-friendly website with e-commerce capability. Web pages should include pictures of our product, bio/history of operator/Heron cooperation, detailed description of the product, shopping cart. Paypal, major credit cards accepted.

Facts about the store: 4127 N. Larkdale Rd Suite 260 Indianapolis, IN 46219 #317-555-0182. Domain name we would like is www.slumbernook.example. If this domain is already taken, we would like www.slumbernook-shop.example. Features that set Slumber Nook apart from competitors: local delivery within a day, product stored on site and available to take home the same day, vacuumed sealed boxed option for same day take home, dual-sided mattress options (firm/plush), locally owned/operated, locally manufactured (Fort Wayne, IN), FoamVeri-CA certified (info link for FoamVeri https://foamveri.example/ )

Here is the website we will be using for background information/pictures. Please check out the descriptions/pictures for ideas. We are waiting to hear back from Heron's owners in regard to permission using their actual photos.

https://www.heronbeds.example/products/mattresses/

https://www.heronbeds.example/products/futons/

We will be attaching a price list. We will probably have more products/info to add. We are also attaching our logo which was designed with Artisan Hive but we need to get a higher res copy from the designer.

We also would like an email associated with the website/company: info@slumbernook.example ( we are not sure how an email gets set up)

Target Market(s)

mattress shoppers!

Industry/Entity Type

Retail

Coding

Coded - Design and coding required

Number of Pages Required

5+ page

Font styles to use
Sans Serif

Colors
0455a3
cfdeed
eaf1f7

Requirements
Must have
• e-commerce/shopping cart, pictures (pets in beds, RVs, futons etc - please see websites listed in project description), watermark, user friendly, product information (please see web site listed in project description), crisp pictures/lines, should emote a sense of comfort, ability to be viewed on mobile device
• link to follow on FB/IG https://www.facebook.com/slumbernook/ IG: slumbernook
• ability for the customer/viewer to "contact us now/ask questions". Ability for customers to leave reviews on products/star rating
• prices should be listed next to product, not "see price in cart", ability to "sort" by price low-high, filter options (i.e. type: pet, RV, futon, mattress,) then a filter option for mattress size (twin, full, queen, king)
Should not have
• rollover/mouse over

```html
<!DOCTYPE html>
<html lang="en">
<head>
<meta charset="utf-8">
<title>Slumber Nook – Mattresses</title>
<link href="https://fonts.googleapis.com/css2?family=Lato:wght@400;700&display=swap" rel="stylesheet">
<style>
:root{
  --blue:#0455a3;
  --accent:#2b8fd6;
  --band:#cfdeed;
  --pale:#eaf1f7;
  --ink:#1d1d1d;
  --muted:#8a8a8a;
  --footer:#111418;
  --white:#ffffff;
}
*{margin:0;padding:0;box-sizing:border-box}
html,body{width:1200px;height:4870px;overflow:hidden}
body{position:relative;font-family:'Lato',sans-serif;color:var(--ink);background:var(--white)}
.abs{position:absolute}
.btn{position:absolute;background:var(--blue);color:var(--white);font-size:11px;font-weight:700;letter-spacing:.3px;display:flex;align-items:center;justify-content:center;text-transform:uppercase}
.section-title{position:absolute;left:0;width:1200px;text-align:center;font-size:38px;font-weight:700;color:var(--ink)}

/* header */
.ship-tag{left:145px;top:27px;width:110px;height:22px;border:1.5px solid var(--accent);font-size:10px;display:flex;align-items:center;justify-content:center;gap:5px;color:#333;z-index:2}
.brand{left:0;width:1200px;top:20px;text-align:center;font-size:21px;font-weight:700;letter-spacing:1px;z-index:2}
.phone{left:890px;top:29px;font-size:11px;display:flex;gap:6px;align-items:center;z-index:2}
.cart-tag{left:998px;top:27px;width:60px;height:22px;border:1.5px solid var(--accent);font-size:10px;display:flex;align-items:center;justify-content:center;gap:4px;z-index:2}
.main-nav{left:0;width:1200px;top:79px;display:flex;justify-content:center;gap:22px;font-size:11px;color:#333;z-index:2}
.main-nav .current{color:var(--accent)}

/* hero */
.hero-photo{left:0;top:0;width:1200px;height:840px;background:
  radial-gradient(ellipse 420px 260px at 880px 300px,#e9d3c7 0%,rgba(233,211,199,0) 70%),
  linear-gradient(180deg,#ffffff 0%,#eef0f3 12%,#e3e7ed 45%,#eef0f3 75%,#ffffff 100%)}
.hero-frame{left:166px;top:250px;width:470px;height:440px;border:11px solid var(--band)}
.hero-title{left:202px;top:493px;font-size:39px;font-weight:700;line-height:47px;color:#222}
.hero-dots{left:578px;top:764px;display:flex;gap:5px;align-items:center}
.hero-dots span{width:5px;height:5px;background:#222}
.hero-dots .on{width:18px;height:4px;background:var(--accent)}

/* history */
.history-box{left:99px;top:905px;width:598px;height:500px;background:var(--band)}
.history-photo{left:625px;top:945px;width:575px;height:405px;border-radius:18px 0 0 18px;background:linear-gradient(160deg,#5f5c59 0%,#7a7672 35%,#a39e98 60%,#8b8782 80%,#4f4c49 100%)}
.history-title{left:148px;top:990px;font-size:38px;font-weight:700}
.history-text{left:148px;top:1061px;width:437px;font-size:12.5px;line-height:17px;text-align:justify;color:#222}

/* product cards */
.card-photo{position:absolute;width:296px;height:194px;border:2px solid #ddd}
.card-name{position:absolute;width:296px;text-align:center;font-size:13.5px;color:#222}
.card-sub{position:absolute;width:296px;text-align:center;font-size:11px;color:var(--muted)}
.series-name{position:absolute;display:flex;align-items:center;gap:8px;font-size:16px;font-weight:700;color:#555}
.series-name i{width:14px;height:14px;border-radius:50%;background:var(--blue);display:block}
.divider{left:146px;top:2050px;width:912px;height:2px;background:#333}

/* features */
.features-band{left:0;top:2593px;width:1200px;height:635px;background:var(--band)}
.feature-icon{position:absolute;width:124px;height:124px;border:8px solid var(--white);display:flex;align-items:center;justify-content:center}
.feature-label{position:absolute;width:210px;text-align:center;font-size:13px;line-height:17px;color:#222}
.cert-box{position:absolute;left:810px;top:2752px;width:243px;height:341px;border:8px solid var(--white);display:flex;align-items:center;justify-content:center}
.cert-seal{width:150px;height:150px;border-radius:50%;background:#3d8d3f;border:12px solid #ffffff;box-shadow:0 0 0 6px #3d8d3f}

/* reviews */
.review-quote{left:250px;top:3357px;width:700px;text-align:center;font-size:12.5px;font-weight:700;line-height:18px}
.quote-mark{font-size:60px;font-weight:700;line-height:1}
.stars{left:0;width:1200px;top:3410px;text-align:center;color:#f08a24;font-size:13px;letter-spacing:2px}
.reviewer{left:0;width:1200px;top:3440px;text-align:center;font-size:18px;font-weight:700}
.review-dots{left:580px;top:3487px;display:flex;gap:9px}
.review-dots span{width:4px;height:4px;border-radius:50%;background:var(--accent)}

/* contact */
.contact-box{left:342px;top:3563px;width:520px;height:582px;background:var(--pale)}
.contact-title{left:342px;width:520px;top:3612px;text-align:center;font-size:38px;font-weight:400}
.field{position:absolute;left:382px;width:440px;background:var(--white);font-size:10px;color:#999;padding:20px 24px}

/* map */
.map-area{left:0;top:4220px;width:1200px;height:275px;background:linear-gradient(90deg,#dceccd 0%,#dceccd 21%,#eceae6 22%,#eceae6 100%)}

/* footer */
.site-footer{left:0;top:4495px;width:1200px;height:375px;background:var(--footer);color:var(--white)}
.foot-brand{left:81px;top:4556px;font-size:19px;font-weight:700;letter-spacing:1px;color:var(--white)}
.foot-about{left:81px;top:4611px;width:275px;font-size:10.5px;line-height:14px;color:#e5e5e5}
.foot-more{left:81px;top:4676px;font-size:10.5px;color:var(--accent);text-decoration:underline}
.foot-social{left:84px;top:4704px;width:24px;height:24px;border:1.5px solid #fff;border-radius:50%;display:flex;align-items:center;justify-content:center}
.foot-heading{position:absolute;top:4553px;font-size:26px;color:var(--white)}
.foot-list{position:absolute;top:4614px;list-style:none;font-size:10.5px;color:#e5e5e5}
.foot-list li{height:29px;padding-left:22px;position:relative}
.foot-list li::before{content:"";position:absolute;left:0;top:5px;width:4px;height:4px;border-radius:50%;background:#fff}
.foot-contact{position:absolute;left:920px;font-size:10.5px;line-height:13px;color:#e5e5e5;display:flex;gap:12px}
.foot-rule{left:81px;top:4780px;width:1040px;height:1px;background:#666}
.copyright{left:81px;top:4808px;font-size:12px;color:#e5e5e5}
.pay-cards{left:965px;top:4805px;display:flex;gap:6px}
.pay-cards span{width:34px;height:22px;border-radius:3px;display:block}
</style>
</head>
<body>

<!-- Header -->
<div class="abs ship-tag">Free Shipping
  <svg width="16" height="11" viewBox="0 0 16 11" fill="none" stroke="#333" stroke-width="1"><rect x="1" y="1" width="9" height="6"/><path d="M10 3h3l2 2v2h-5"/><circle cx="4" cy="9" r="1.3"/><circle cx="12" cy="9" r="1.3"/></svg>
</div>
<div class="abs brand">SLUMBER NOOK</div>
<div class="abs phone">
  <svg width="13" height="13" viewBox="0 0 24 24" fill="none" stroke="#333" stroke-width="2"><path d="M22 16.9v3a2 2 0 0 1-2.2 2 19.8 19.8 0 0 1-8.6-3.1 19.5 19.5 0 0 1-6-6A19.8 19.8 0 0 1 2.1 4.2 2 2 0 0 1 4.1 2h3a2 2 0 0 1 2 1.7c.1 1 .4 1.9.7 2.8a2 2 0 0 1-.5 2.1L8 9.9a16 16 0 0 0 6 6l1.3-1.3a2 2 0 0 1 2.1-.4c.9.3 1.8.6 2.8.7a2 2 0 0 1 1.7 2z"/></svg>
  317-555-0182
</div>
<div class="abs cart-tag">Cart
  <svg width="13" height="12" viewBox="0 0 24 22" fill="none" stroke="#333" stroke-width="2"><path d="M1 1h4l3 13h12l3-9H6"/><circle cx="9" cy="19" r="1.6"/><circle cx="19" cy="19" r="1.6"/></svg>
</div>
<nav class="abs main-nav">
  <span class="current">Home</span><span>Mattresses</span><span>Our History</span><span>Our Store</span><span>Reviews</span><span>Contact us</span>
</nav>

<!-- Hero -->
<div class="abs hero-photo" role="img" aria-label="Photo of a woman sleeping peacefully on white bedding"></div>
<div class="abs hero-frame"></div>
<h1 class="abs hero-title">A Mattresses For<br>Every Kind Of Sleepers</h1>
<div class="btn" style="left:205px;top:610px;width:167px;height:41px">Shop Now</div>
<div class="abs hero-dots"><span class="on"></span><span></span><span></span></div>

<!-- History -->
<div class="abs history-box"></div>
<div class="abs history-photo" role="img" aria-label="Photo of a grey upholstered bed with a made mattress"></div>
<h2 class="abs history-title">Our History</h2>
<p class="abs history-text">Slumber Nook was founded by two brilliant partners looking to formulate their vision of impeccable customer service and quality product into one store. After working in retail for a combined 30+ years, Slumber Nook's founders wanted to put their knowledge, skill and experience to work for themselves. After researching exceptional products to showcase in their store, Heron mattresses stood out for both its comfort and quality, not to mention its sleek design. When it was learned that Heron Mattresses are made right here in Indiana, the choice was clear. Slumber Nook has partnered with Heron Mattresses to bring you affordable comfort right here in Indy. Come find out where sleep happens.</p>
<div class="btn" style="left:151px;top:1282px;width:167px;height:43px">Read More</div>

<!-- Mattress Collection -->
<h2 class="section-title" style="top:1498px">Mattress Collection</h2>
<div class="series-name" style="left:222px;top:1604px"><span>BLUE HERON</span><i></i></div>
<div class="series-name" style="left:528px;top:1604px"><span>WHITE HERON</span><i></i></div>
<div class="series-name" style="left:836px;top:1604px;color:#111"><span>NIGHT HERON</span><i></i></div>

<div class="card-photo" style="left:146px;top:1658px;background:linear-gradient(180deg,#cfc7bd 0%,#bdb3a7 45%,#e4e2df 60%,#8f857a 100%)" role="img" aria-label="Photo of a Blue Heron mattress on a black metal frame"></div>
<div class="card-photo" style="left:456px;top:1658px;background:linear-gradient(180deg,#9a8270 0%,#7d6757 45%,#2a2a2c 62%,#3b3532 100%)" role="img" aria-label="Photo of a White Heron mattress in front of a brick wall"></div>
<div class="card-photo" style="left:765px;top:1658px;background:linear-gradient(180deg,#c9ccc5 0%,#b7bbb3 40%,#3c4450 60%,#6d6f72 100%)" role="img" aria-label="Photo of a Night Heron mattress in a bright room"></div>

<div class="card-name" style="left:146px;top:1865px;font-weight:700">Blue Heron (Value) Collection</div>
<div class="card-name" style="left:456px;top:1865px">White Heron (Mid-Value) Collection</div>
<div class="card-name" style="left:765px;top:1865px">Night Heron (High-End) Collection</div>
<div class="card-sub" style="left:146px;top:1886px">A Penny For Your Dreams</div>
<div class="card-sub" style="left:456px;top:1886px">Value You Will Feel All Night Long!</div>
<div class="card-sub" style="left:765px;top:1886px">Comfort You Can Feel With Your Eyes Closed!</div>
<div class="btn" style="left:210px;top:1927px;width:167px;height:43px">View Now</div>
<div class="btn" style="left:520px;top:1927px;width:167px;height:43px">View Now</div>
<div class="btn" style="left:829px;top:1927px;width:167px;height:43px">View Now</div>

<div class="abs divider"></div>

<!-- Other mattresses -->
<h2 class="section-title" style="top:2100px">We also Mattresses Offer</h2>
<div class="card-photo" style="left:146px;top:2185px;background:linear-gradient(180deg,#2f4a66 0%,#4c6784 45%,#b79a74 65%,#4f4436 100%)" role="img" aria-label="Photo of a vintage travel trailer at dusk with a patio set"></div>
<div class="card-photo" style="left:456px;top:2185px;background:linear-gradient(180deg,#bcb6ad 0%,#a9a39a 50%,#6c9fc2 75%,#8d867b 100%)" role="img" aria-label="Photo of a pet bed with a blue cushion"></div>
<div class="card-photo" style="left:765px;top:2185px;background:linear-gradient(180deg,#8a8a8a 0%,#5e5e5e 50%,#3a3a3c 75%,#6a6a6a 100%)" role="img" aria-label="Photo of a grey futon in a loft room"></div>
<div class="card-name" style="left:146px;top:2394px">Cozy Trail RV's</div>
<div class="card-name" style="left:456px;top:2394px">Pet Mattress</div>
<div class="card-name" style="left:765px;top:2394px">Loft Line Futons</div>
<div class="card-sub" style="left:146px;top:2415px">Journey Mattress Collection</div>
<div class="card-sub" style="left:456px;top:2415px">Pet Mattress</div>
<div class="card-sub" style="left:765px;top:2415px">Futons</div>
<div class="btn" style="left:210px;top:2455px;width:167px;height:43px">View Now</div>
<div class="btn" style="left:520px;top:2455px;width:167px;height:43px">View Now</div>
<div class="btn" style="left:829px;top:2455px;width:167px;height:43px">View Now</div>

<!-- Features -->
<div class="abs features-band"></div>
<h2 class="section-title" style="top:2640px">Slumber Nook Features</h2>

<div class="feature-icon" style="left:167px;top:2752px">
  <svg width="66" height="44" viewBox="0 0 66 44" fill="none" stroke="#222" stroke-width="2"><rect x="2" y="4" width="40" height="28"/><path d="M42 12h12l8 10v10H42"/><circle cx="14" cy="36" r="5" fill="#cfdeed"/><circle cx="52" cy="36" r="5" fill="#cfdeed"/><path d="M14 18l6 6 10-10"/></svg>
</div>
<div class="feature-icon" style="left:394px;top:2752px">
  <svg width="52" height="46" viewBox="0 0 52 46" fill="none" stroke="#222" stroke-width="2.4"><path d="M2 3h8l6 28h28l6-20H12"/><circle cx="20" cy="40" r="4"/><circle cx="40" cy="40" r="4"/></svg>
</div>
<div class="feature-icon" style="left:605px;top:2752px">
  <svg width="48" height="48" viewBox="0 0 48 48" fill="none" stroke="#222" stroke-width="2"><rect x="3" y="3" width="42" height="42"/><path d="M17 3v14h14V3"/><path d="M16 38V28M13 31l3-3 3 3M32 38V28M29 31l3-3 3 3"/></svg>
</div>
<div class="cert-box"><div class="cert-seal" role="img" aria-label="FoamVeri-CA certification seal"></div></div>

<div class="feature-label" style="left:124px;top:2890px">Local delivery within a day</div>
<div class="feature-label" style="left:351px;top:2890px">Product stored on site and available to take home the same day</div>
<div class="feature-label" style="left:562px;top:2890px">Vacuumed sealed boxed option for same day take home</div>

<div class="feature-icon" style="left:167px;top:2970px">
  <svg width="52" height="46" viewBox="0 0 52 46" fill="none" stroke="#222" stroke-width="2"><path d="M2 44V24l12-8v8l12-8v8l12-8V2h8v42z"/><rect x="10" y="32" width="6" height="6"/><rect x="22" y="32" width="6" height="6"/></svg>
</div>
<div class="feature-icon" style="left:394px;top:2970px">
  <svg width="54" height="50" viewBox="0 0 54 50" fill="none" stroke="#222" stroke-width="2"><circle cx="27" cy="18" r="7"/><path d="M27 4v5M27 27v5M13 18h5M36 18h5M17 8l4 4M33 24l4 4M37 8l-4 4M21 24l-4 4"/><rect x="6" y="38" width="42" height="9" rx="4.5"/><circle cx="14" cy="42.5" r="1.5"/><circle cx="22" cy="42.5" r="1.5"/><circle cx="32" cy="42.5" r="1.5"/><circle cx="40" cy="42.5" r="1.5"/></svg>
</div>
<div class="feature-icon" style="left:605px;top:2970px">
  <svg width="56" height="40" viewBox="0 0 56 40" fill="none" stroke="#222" stroke-width="2"><path d="M6 22V4h44v18"/><rect x="12" y="12" width="12" height="8" rx="2"/><rect x="32" y="12" width="12" height="8" rx="2"/><rect x="2" y="22" width="52" height="10"/><path d="M6 32v6M50 32v6"/></svg>
</div>
<div class="feature-label" style="left:124px;top:3110px">Locally owned/operated</div>
<div class="feature-label" style="left:351px;top:3108px">Locally manufactured<br>(Fort Wayne, IN)</div>
<div class="feature-label" style="left:562px;top:3108px">Dual-sided mattress<br>options (firm/plush)</div>
<div class="feature-label" style="left:826px;top:3107px">FoamVeri-CA certified</div>

<!-- Reviews -->
<h2 class="section-title" style="top:3280px">Customer`s Reviews</h2>
<div class="abs quote-mark" style="left:216px;top:3330px">“</div>
<p class="abs review-quote">Lorem Ipsum is simply dummy text of the printing and typesetting industry. Lorem Ipsum has been the industry's standard dummy text ever since the 1500s,</p>
<div class="abs quote-mark" style="left:950px;top:3350px">”</div>
<div class="abs stars">★★★★★</div>
<div class="abs reviewer">Dana Mercer</div>
<div class="abs review-dots"><span></span><span></span><span></span></div>

<!-- Contact -->
<div class="abs contact-box"></div>
<h2 class="abs contact-title">Contact us</h2>
<div class="field" style="top:3680px;height:55px">Full Name</div>
<div class="field" style="top:3747px;height:55px">Email Address</div>
<div class="field" style="top:3814px;height:55px">Phone#</div>
<div class="field" style="top:3881px;height:130px">Massage</div>
<div class="btn" style="left:516px;top:4030px;width:166px;height:42px">Submit Now</div>

<!-- Map -->
<div class="abs map-area" role="img" aria-label="Street map showing the store location in south Indianapolis"></div>

<!-- Footer -->
<footer class="abs site-footer"></footer>
<div class="abs foot-brand">SLUMBER NOOK</div>
<p class="abs foot-about">Slumber Nook was founded by two brilliant partners looking to formulate their vision of impeccable customer service and quality product into one store.</p>
<div class="abs foot-more">READ MORE</div>
<div class="abs foot-social">
  <svg width="10" height="12" viewBox="0 0 10 12" fill="none" stroke="#fff" stroke-width="1.2"><circle cx="5" cy="6" r="3"/></svg>
</div>

<div class="foot-heading" style="left:435px">Quick Link</div>
<ul class="foot-list" style="left:438px"><li>Home</li><li>Our Products</li><li>Our History</li><li>Our Store</li><li>Contact us</li></ul>

<div class="foot-heading" style="left:692px">Account</div>
<ul class="foot-list" style="left:690px"><li>Login</li><li>Register</li><li>My Profile</li><li>My Cart</li><li>Checkout</li></ul>

<div class="foot-heading" style="left:920px">Contact</div>
<div class="foot-contact" style="top:4613px">
  <svg width="14" height="14" viewBox="0 0 24 24" fill="none" stroke="#fff" stroke-width="2"><path d="M22 16.9v3a2 2 0 0 1-2.2 2 19.8 19.8 0 0 1-8.6-3.1 19.5 19.5 0 0 1-6-6A19.8 19.8 0 0 1 2.1 4.2 2 2 0 0 1 4.1 2h3a2 2 0 0 1 2 1.7c.1 1 .4 1.9.7 2.8a2 2 0 0 1-.5 2.1L8 9.9a16 16 0 0 0 6 6l1.3-1.3a2 2 0 0 1 2.1-.4c.9.3 1.8.6 2.8.7a2 2 0 0 1 1.7 2z"/></svg>
  <span>317-555-0182</span>
</div>
<div class="foot-contact" style="top:4656px">
  <svg width="14" height="12" viewBox="0 0 24 18" fill="none" stroke="#fff" stroke-width="2"><rect x="1" y="1" width="22" height="16"/><path d="M1 1l11 9 11-9"/></svg>
  <span>info@slumbernook.example</span>
</div>
<div class="foot-contact" style="top:4694px">
  <svg width="14" height="16" viewBox="0 0 20 24" fill="none" stroke="#fff" stroke-width="2"><path d="M10 23s8-8 8-13a8 8 0 0 0-16 0c0 5 8 13 8 13z"/><circle cx="10" cy="10" r="3"/></svg>
  <span>4127 N. Larkdale Rd Suite 260<br>Indianapolis, IN 46219</span>
</div>

<div class="abs foot-rule"></div>
<div class="abs copyright">Copyright © 2019 Slumber Nook. All Right Reserved</div>
<div class="abs pay-cards" role="img" aria-label="Accepted payment methods">
  <span style="background:#1f4fa0"></span>
  <span style="background:#1a5fd0"></span>
  <span style="background:#e8e8e8"></span>
  <span style="background:#3a86d4"></span>
</div>

</body>
</html>
```